Tallowreed Advisory Partners Business Card Design

We have the logo we just need someone to design a modern business card design.

Name: Desmond Munkalt
Phone: 3055550148
Mobile: 9175550193
Web:www.tallowreedadvisory.example
email: dmunkalt@tallowreedadvisory.example
Company: Tallowreed Advisory Partners
Title: CEO

Address: 718 Quillmore Ave, Miami, Florida 33190

Target Market(s)

companies over 100 employees

Industry/Entity Type

Business

```html
<!DOCTYPE html>
<html lang="en">
<head>
<meta charset="utf-8">
<title>Tallowreed Advisory Partners – Business Card</title>
<link rel="stylesheet" href="https://fonts.googleapis.com/css2?family=Roboto:wght@400;700&family=Roboto+Condensed:wght@400&display=swap">
<style>
  :root {
    --backdrop: #e6e3de;
    --card-black: #121212;
    --card-charcoal: #2a2a2a;
    --card-grey: #4a4a4a;
    --brand-blue: #2aa7e6;
    --brand-blue-deep: #1583c7;
    --text-white: #ffffff;
    --text-soft: #d6d6d6;
  }
  * { box-sizing: border-box; margin: 0; padding: 0; }
  html, body { width: 1200px; height: 913px; overflow: hidden; }
  body {
    background: var(--backdrop);
    font-family: "Roboto", Arial, sans-serif;
    position: relative;
  }
  .card {
    position: absolute;
    width: 560px;
    height: 320px;
    border-radius: 4px;
    overflow: hidden;
    box-shadow: 0 10px 24px rgba(0,0,0,0.25);
  }
  .card-front {
    left: 70px; top: 80px;
    background: linear-gradient(135deg, var(--card-charcoal) 0%, var(--card-black) 60%, #1c1c1c 100%);
    display: flex; align-items: center; justify-content: center;
  }
  .card-back {
    left: 570px; top: 510px;
    background: var(--card-black);
  }
  .wordmark {
    display: flex; align-items: center; gap: 16px;
  }
  .wordmark-dot {
    width: 58px; height: 58px; border-radius: 50%;
    background: var(--brand-blue);
    flex: none;
  }
  .wordmark-name {
    color: var(--text-white);
    font-weight: 700;
    font-size: 26px;
    letter-spacing: 0.5px;
    line-height: 1.1;
  }
  .card-back .back-art { position: absolute; inset: 0; }
  .card-back .wordmark {
    position: absolute; right: 40px; top: 34px;
    gap: 12px;
  }
  .card-back .wordmark-dot { width: 44px; height: 44px; }
  .card-back .wordmark-name { font-size: 19px; }
  .holder {
    position: absolute; right: 40px; top: 132px; text-align: right;
  }
  .holder-name {
    color: var(--brand-blue);
    font-weight: 700; font-size: 17px;
  }
  .holder-title {
    color: var(--text-soft);
    font-size: 12px; margin-top: 2px;
  }
  .contact-list {
    position: absolute; left: 32px; bottom: 26px;
    list-style: none;
    font-family: "Roboto Condensed", Arial, sans-serif;
    font-size: 13px; color: var(--text-white);
  }
  .contact-list li {
    display: flex; align-items: center; gap: 10px;
    height: 19px;
  }
  .contact-list svg { width: 12px; height: 12px; flex: none; fill: var(--brand-blue); }
</style>
</head>
<body>

<section class="card card-front" aria-label="Card front">
  <div class="wordmark">
    <span class="wordmark-dot"></span>
    <span class="wordmark-name">Tallowreed Advisory Partners</span>
  </div>
</section>

<section class="card card-back" aria-label="Card back">
  <svg class="back-art" viewBox="0 0 560 320" preserveAspectRatio="none" aria-hidden="true">
    <defs>
      <linearGradient id="upper" x1="0" y1="0" x2="1" y2="1">
        <stop offset="0" stop-color="#262626"/>
        <stop offset="1" stop-color="#0f0f0f"/>
      </linearGradient>
      <linearGradient id="lower" x1="0" y1="0" x2="0" y2="1">
        <stop offset="0" stop-color="#555555"/>
        <stop offset="1" stop-color="#3a3a3a"/>
      </linearGradient>
    </defs>
    <rect width="560" height="320" fill="url(#lower)"/>
    <path d="M0 0 H560 V58 C430 120 300 170 0 158 Z" fill="url(#upper)"/>
    <path d="M0 158 C300 170 430 120 560 58" fill="none" stroke="var(--brand-blue)" stroke-width="5"/>
    <path d="M0 164 C300 176 430 126 560 64" fill="none" stroke="var(--brand-blue-deep)" stroke-width="1.5" opacity="0.7"/>
  </svg>

  <div class="wordmark">
    <span class="wordmark-dot"></span>
    <span class="wordmark-name">Tallowreed Advisory Partners</span>
  </div>

  <div class="holder">
    <p class="holder-name">Desmond Munkalt</p>
    <p class="holder-title">CEO</p>
  </div>

  <ul class="contact-list">
    <li><svg viewBox="0 0 24 24"><path d="M6.6 10.8a15 15 0 006.6 6.6l2.2-2.2a1 1 0 011-.25 11.4 11.4 0 003.6.57 1 1 0 011 1V20a1 1 0 01-1 1A17 17 0 013 4a1 1 0 011-1h3.5a1 1 0 011 1 11.4 11.4 0 00.57 3.6 1 1 0 01-.25 1z"/></svg>3055550148</li>
    <li><svg viewBox="0 0 24 24"><path d="M7 1h10a2 2 0 012 2v18a2 2 0 01-2 2H7a2 2 0 01-2-2V3a2 2 0 012-2zm0 3v14h10V4z"/></svg>9175550193</li>
    <li><svg viewBox="0 0 24 24"><path d="M12 2a10 10 0 100 20 10 10 0 000-20zm6.9 6h-3a15 15 0 00-1.4-3.6A8 8 0 0118.9 8zM12 4a13 13 0 011.9 4h-3.8A13 13 0 0112 4zM4.3 14a8 8 0 010-4h3.4a16 16 0 000 4zm.8 2h3a15 15 0 001.4 3.6A8 8 0 015.1 16zm3-8h-3a8 8 0 014.4-3.6A15 15 0 008.1 8zM12 20a13 13 0 01-1.9-4h3.8A13 13 0 0112 20zm2.3-6H9.7a14 14 0 010-4h4.6a14 14 0 010 4zm.2 5.6a15 15 0 001.4-3.6h3a8 8 0 01-4.4 3.6zm1.8-5.6a16 16 0 000-4h3.4a8 8 0 010 4z"/></svg>www.tallowreedadvisory.example</li>
    <li><svg viewBox="0 0 24 24"><path d="M2 5h20v14H2zm2 2v.5l8 5 8-5V7l-8 5z"/></svg>dmunkalt@tallowreedadvisory.example</li>
    <li><svg viewBox="0 0 24 24"><path d="M12 2a7 7 0 00-7 7c0 5.2 7 13 7 13s7-7.8 7-13a7 7 0 00-7-7zm0 9.5A2.5 2.5 0 1112 6.5a2.5 2.5 0 010 5z"/></svg>718 Quillmore Ave, Miami, Florida 33190</li>
  </ul>
</section>

</body>
</html>
```